Business card design for Allied Healthcare provider

We would like a design for front and back of business cards. The design must resonate with all levels of customers from patients, to other health providers and medical. Must also resonate with corporate customers

Target Market(s)

patients, medical practitioners, other health providers and corporate.

Industry/Entity Type

healthcare

Contact Information for Business Card

name, logo, phone and fax numbers, email, website

Requirements
Must have
• not allowing me to change this, but the card must be double sided!! Please take note
Nice to have
• a fresh yet bold design to catch attention.

```html
<!DOCTYPE html>
<html lang="en">
<head>
<meta charset="utf-8">
<title>vitalmeld business card</title>
<link href="https://fonts.googleapis.com/css2?family=Poppins:wght@400;500;600;700&display=swap" rel="stylesheet">
<style>
  :root {
    --navy: #1b2b5e;
    --navy-deep: #17264f;
    --gold: #fbb426;
    --ink: #3a3f4a;
    --paper: #ffffff;
    --stage: #2a2a2c;
  }
  * { box-sizing: border-box; margin: 0; padding: 0; }
  html, body { width: 1200px; height: 900px; overflow: hidden; }
  body {
    background: var(--stage);
    font-family: "Poppins", sans-serif;
    position: relative;
  }
  .card {
    position: absolute;
    left: 250px;
    width: 700px;
    height: 400px;
    overflow: hidden;
  }
  .card-front { top: 35px; background: var(--paper); }
  .card-back { top: 465px; background: var(--navy); }

  .front-swoosh { position: absolute; inset: 0; }

  .brand {
    position: absolute;
    display: flex;
    align-items: center;
    gap: 10px;
  }
  .brand-mark {
    width: 16px; height: 16px;
    border-radius: 50%;
    background: var(--gold);
  }
  .brand-name {
    font-weight: 600;
    letter-spacing: 0.5px;
  }
  .card-front .brand { left: 44px; top: 118px; }
  .card-front .brand-name { font-size: 46px; color: var(--navy); }
  .tagline {
    position: absolute;
    left: 72px; top: 180px;
    font-size: 15px;
    color: var(--gold);
    letter-spacing: 0.5px;
  }

  .divider {
    position: absolute;
    left: 402px; top: 100px;
    width: 2px; height: 135px;
    background: var(--navy);
  }
  .contact {
    position: absolute;
    left: 422px; top: 100px;
    color: var(--ink);
  }
  .contact-name {
    font-size: 22px;
    font-weight: 700;
    color: var(--navy);
    letter-spacing: 0.5px;
    line-height: 1.1;
  }
  .contact-role { font-size: 15px; margin-bottom: 10px; }
  .contact-list { list-style: none; font-size: 14px; line-height: 1.55; }
  .contact-list li { display: flex; align-items: center; gap: 8px; }
  .contact-list svg { width: 13px; height: 13px; fill: var(--gold); flex: none; }

  .website {
    position: absolute;
    left: 34px; top: 290px;
    font-size: 13px;
    color: var(--paper);
    letter-spacing: 0.5px;
  }

  .back-field { position: absolute; inset: 0; background: var(--navy); }
  .card-back .brand { right: 40px; bottom: 50px; }
  .card-back .brand-name { font-size: 40px; color: var(--paper); }
</style>
</head>
<body>

<section class="card card-front" aria-label="Card front">
  <svg class="front-swoosh" viewBox="0 0 700 400" preserveAspectRatio="none" aria-hidden="true">
    <path d="M0,238 C190,226 290,300 415,350 C520,392 620,384 700,366 L700,400 L0,400 Z" fill="var(--gold)"/>
    <path d="M0,254 C195,246 285,318 395,362 C480,394 600,400 700,400 L0,400 Z" fill="var(--navy)"/>
  </svg>

  <div class="brand">
    <span class="brand-mark"></span>
    <span class="brand-name">vitalmeld</span>
  </div>
  <p class="tagline">recovery · support · health</p>

  <div class="divider"></div>
  <div class="contact">
    <p class="contact-name">DANA WHITFIELD</p>
    <p class="contact-role">President</p>
    <ul class="contact-list">
      <li>
        <svg viewBox="0 0 24 24"><path d="M6.6 10.8a15.1 15.1 0 0 0 6.6 6.6l2.2-2.2a1 1 0 0 1 1-.25 11.4 11.4 0 0 0 3.6.57 1 1 0 0 1 1 1V20a1 1 0 0 1-1 1A17 17 0 0 1 3 4a1 1 0 0 1 1-1h3.5a1 1 0 0 1 1 1c0 1.25.2 2.45.57 3.57a1 1 0 0 1-.25 1z"/></svg>
        555-014-2287
      </li>
      <li>
        <svg viewBox="0 0 24 24"><path d="M6 2h10l2 2v5H6z M3 10h18a1 1 0 0 1 1 1v8a1 1 0 0 1-1 1H3a1 1 0 0 1-1-1v-8a1 1 0 0 1 1-1z"/></svg>
        555-014-2288
      </li>
      <li>
        <svg viewBox="0 0 24 24"><path d="M2 5h20v14H2z M2 5l10 8 10-8" /></svg>
        info@vitalmeldcare.com
      </li>
    </ul>
  </div>

  <p class="website">www.vitalmeld.com</p>
</section>

<section class="card card-back" aria-label="Card back">
  <div class="back-field" role="img" aria-label="Navy background with a faint embossed repeating brand pattern"></div>
  <div class="brand">
    <span class="brand-mark"></span>
    <span class="brand-name">vitalmeld</span>
  </div>
</section>

</body>
</html>
```